Need Business Cards for my Business

email address: rkpmarlowhollowworks@vendrimail.com
web address: rkpmarlowhollowworks.net
Slogan: We offer various QVN licenses
Rowland K. Pemberly
Please stick with colors of Company Logo
would like the card to be more of the color example of the logo.
If you need PDF copy of logo email me at the above account.
Creative control rests with you.

Industry/Entity Type

Business

Contact Information for Business Card

I am a minimalist, but would like something to pop and stand out amongst other cards, make it memorable.

Font styles to use
Serif
Decorative
Script

```html
<!DOCTYPE html>
<html lang="en">
<head>
<meta charset="utf-8">
<title>Marlow Hollow Works — Business Card</title>
<link href="https://fonts.googleapis.com/css2?family=Quicksand:wght@500;700&display=swap" rel="stylesheet">
<style>
  :root {
    --stage: #e3e3e3;
    --stage-glow: #ececec;
    --blue-light: #2f88f6;
    --blue-mid: #1a5fd6;
    --blue-deep: #0a2c86;
    --navy-text: #163a96;
    --white: #ffffff;
    --ink: #111111;
  }
  * { margin: 0; padding: 0; box-sizing: border-box; }
  html, body { width: 1200px; height: 849px; overflow: hidden; }
  body {
    background: radial-gradient(circle at 50% 48%, var(--stage-glow) 0, var(--stage-glow) 330px, var(--stage) 332px);
    font-family: "Quicksand", sans-serif;
    position: relative;
  }

  .brand-showcase {
    position: absolute;
    left: 0; top: 150px;
    width: 1200px;
    text-align: center;
    color: var(--white);
    font-weight: 700;
    font-size: 78px;
    letter-spacing: 2px;
    line-height: 1;
  }
  .brand-showcase .tag {
    display: block;
    margin-top: 18px;
    font-size: 40px;
    letter-spacing: 4px;
  }

  .card {
    position: absolute;
    top: 412px;
    width: 345px;
    height: 222px;
    border-radius: 24px;
    overflow: hidden;
    box-shadow: 0 6px 12px rgba(0,0,0,0.28);
  }

  .card-front {
    left: 204px;
    background: linear-gradient(90deg, var(--blue-light) 0%, var(--blue-mid) 55%, var(--blue-deep) 100%);
  }
  .card-front .brand-band {
    position: absolute;
    left: 0; top: 68px;
    width: 100%; height: 87px;
    background: linear-gradient(90deg, rgba(255,255,255,0.15) 0%, #ffffff 40%, #ffffff 55%, rgba(255,255,255,0.2) 100%);
    display: flex;
    align-items: center;
    justify-content: center;
  }
  .card-front .brand-name {
    color: var(--navy-text);
    font-weight: 700;
    font-size: 21px;
    letter-spacing: 0.5px;
  }

  .card-back {
    left: 617px;
    background: var(--white);
  }
  .card-back .brand-strip {
    position: absolute;
    left: 0; top: 0;
    width: 105px; height: 100%;
    background: linear-gradient(160deg, var(--blue-light) 0%, var(--blue-mid) 50%, var(--blue-deep) 100%);
  }
  .card-back .strip-name {
    position: absolute;
    left: 52px; top: 111px;
    transform: translate(-50%, -50%) rotate(-90deg);
    white-space: nowrap;
    color: var(--white);
    font-weight: 700;
    font-size: 19px;
    letter-spacing: 0.5px;
  }
  .card-back .contact {
    position: absolute;
    left: 121px; top: 56px;
    color: var(--ink);
  }
  .contact .person {
    font-weight: 700;
    font-size: 12.5px;
    margin-bottom: 13px;
  }
  .contact .label,
  .contact .value {
    font-weight: 700;
    font-size: 10px;
    line-height: 13px;
  }
  .contact .value { font-weight: 500; }
  .card-back .slogan {
    position: absolute;
    left: 105px; right: 0; top: 168px;
    text-align: center;
    font-weight: 700;
    font-size: 11px;
    color: var(--ink);
  }
</style>
</head>
<body>

  <div class="brand-showcase">
    Marlow Hollow Works
    <span class="tag">Marlow Hollow Works</span>
  </div>

  <section class="card card-front" aria-label="Card front">
    <div class="brand-band">
      <span class="brand-name">Marlow Hollow Works</span>
    </div>
  </section>

  <section class="card card-back" aria-label="Card back">
    <div class="brand-strip">
      <span class="strip-name">Marlow Hollow Works</span>
    </div>
    <div class="contact">
      <p class="person">Rowland K. Pemberly</p>
      <p class="label">email address:</p>
      <p class="value">rkpmarlowhollowworks@vendrimail.com</p>
      <p class="label">web address:</p>
      <p class="value">rkpmarlowhollowworks.net</p>
    </div>
    <p class="slogan">We offer various QVN licenses</p>
  </section>

</body>
</html>
```